Business card for boutique investment firm

Need a business card designed for our boutique investment firm called "BrightLedger Investment Fee Advisors". We help investors achieve lower fees through negotiation on their behalf. We have a logo to work with and a color palette. The card should incorporate our tag line "Clarity in Every Detail" and space for relevant details. The look and feel should reflect the logo and our brand personality: Humble, Trustworthy, Friendly

Target Market(s)

High net worth investors who are looking for clarity around how they are being charged by their investment advisor

Industry/Entity Type

Boutique

Requirements
Must have
• Logo
Tag line: Clarity in Every Detail
Space for relevant contact details: name, title, phone, email, URL, mailing address

Use these fonts: 'AvantGarde Bk BT' and 'AvantGarde Bk BT Demi'
Use these colors:
Orange = C-0 / M-60 / Y-100 / K-0
Grey = C-0 / M-0 / Y-0 / K-60

```html
<!DOCTYPE html>
<html lang="en">
<head>
<meta charset="utf-8">
<title>BrightLedger Investment Cost Counsel – Business Card</title>
<link rel="stylesheet" href="https://fonts.googleapis.com/css2?family=Questrial&display=swap">
<style>
  :root {
    --orange: #f58220;
    --grey: #808285;
    --paper: #ffffff;
    --backdrop: #e6e6e4;
    --shadow: rgba(0, 0, 0, 0.18);
  }
  * { box-sizing: border-box; margin: 0; padding: 0; }
  html, body {
    width: 1200px;
    height: 1000px;
    overflow: hidden;
    background: var(--backdrop);
    font-family: 'Questrial', sans-serif;
  }
  .canvas {
    width: 1200px;
    height: 1000px;
    display: flex;
    flex-direction: column;
    align-items: center;
    justify-content: center;
    gap: 60px;
  }
  .card {
    position: relative;
    width: 700px;
    height: 400px;
    background: var(--paper);
    overflow: hidden;
    box-shadow: 0 6px 18px var(--shadow);
  }
  .accent-disc {
    position: absolute;
    width: 420px;
    height: 420px;
    border-radius: 50%;
    background: var(--orange);
  }

  .brand__row { display: flex; align-items: center; gap: 14px; }
  .brand__dot {
    border-radius: 50%;
    background: var(--orange);
    flex: none;
  }
  .brand__name {
    line-height: 1;
    color: var(--grey);
    letter-spacing: -0.5px;
    white-space: nowrap;
  }
  .brand__descriptor {
    color: var(--grey);
    margin-top: 4px;
    white-space: nowrap;
  }

  /* Back side */
  .card--back .accent-disc { left: -40px; top: -300px; }
  .card--back .brand { position: absolute; left: 300px; top: 175px; }
  .card--back .brand__dot { width: 46px; height: 46px; }
  .card--back .brand__name { font-size: 46px; }
  .card--back .brand__descriptor { margin-left: 60px; font-size: 15px; letter-spacing: 2.2px; }
  .tagline {
    margin-top: 12px;
    font-size: 17px;
    letter-spacing: 3px;
    color: var(--orange);
    text-transform: uppercase;
    white-space: nowrap;
  }

  /* Contact side */
  .card--front .accent-disc { right: -60px; top: -290px; }
  .card--front .brand { position: absolute; left: 40px; top: 150px; }
  .card--front .brand__dot { width: 40px; height: 40px; }
  .card--front .brand__name { font-size: 38px; }
  .card--front .brand__descriptor { margin-left: 54px; font-size: 13px; letter-spacing: 1.8px; }
  .contact {
    position: absolute;
    left: 400px;
    top: 140px;
    font-size: 15px;
    letter-spacing: 1.5px;
    color: var(--grey);
    line-height: 1.5;
    white-space: nowrap;
  }
  .contact__name { font-size: 18px; text-transform: uppercase; letter-spacing: 2px; }
  .contact__title { color: var(--orange); font-size: 16px; margin-bottom: 16px; }
  .contact__label { color: var(--orange); }
  .contact__company { color: var(--orange); margin-top: 16px; text-transform: uppercase; }
</style>
</head>
<body>
<main class="canvas">
  <section class="card card--back" aria-label="Card back">
    <div class="accent-disc"></div>
    <div class="brand">
      <div class="brand__row">
        <span class="brand__dot"></span>
        <span class="brand__name">BrightLedger</span>
      </div>
      <div class="brand__descriptor">Investment Cost Counsel</div>
      <div class="tagline">Clarity in Every Detail</div>
    </div>
  </section>

  <section class="card card--front" aria-label="Card front">
    <div class="accent-disc"></div>
    <div class="brand">
      <div class="brand__row">
        <span class="brand__dot"></span>
        <span class="brand__name">BrightLedger</span>
      </div>
      <div class="brand__descriptor">Investment Cost Counsel</div>
    </div>
    <div class="contact">
      <p class="contact__name">Your Name</p>
      <p class="contact__title">Title</p>
      <p><span class="contact__label">Phone:</span> 123 567 8900</p>
      <p><span class="contact__label">Email:</span> yourname@brightledger.com</p>
      <p><span class="contact__label">Website:</span> www.brightledger.com</p>
      <p class="contact__company">BrightLedger</p>
      <p>Ste. 12 Washington, NY 1234</p>
    </div>
  </section>
</main>
</body>
</html>
```